Flyer Design Project for our Parenting Psychologists at the Wellmind Counselling Centre

At the Wellmind Counselling Centre we have expert Parenting Psychologists.

Parenting Psychologists provide practical, step by step assistance to parents who are struggling with their children's behavioural and emotional problems.

We need a DL size brochure that will be appealing to parents. The brochure will be on show in schools, kindergartens and GP clinics.

In terms of style it will be in line with our website and stationery that I will attach.

www.wellmindcounsellingcentre.com.au

Hi Everyone,
Thanks for putting forward your proposals, there are a couple there that I am very interested in. I am looking to see if there is a way that I can change my brief to guaranteed as I am definitely going to be using one of the designs for sure.
I have emailed ArtForge and as soon as I get an answer I will change it if I can.
If anyone out there already knows the answer please let me know :-)
Thanks,
Marcie.

Hi Again,

I worked it out myself!!

I have now changed this to a committed project.

Kind regards,
Marcie.

Reason: I have 46 designs now and need more time to work out which is best!

Target Market(s)

The target will be educated professional parents motivated to get professional help. And doctors and teachers who will pass on the brochures 2 parents

Industry/Entity Type

Health

Requirements
Must have
• I want one DL size brochure. Back and front.

We need text (below) and our contact details. Our logo.

6352 1840
Suite 1, 2087 Tamworth Rd, Tamworth North 3118

Text:
Parents want the best for their kids. They want kids that are happy, healthy and well behaved.

So why is it so hard? Parents of toddlers, primary schoolers and teenagers alike say that they are frustrated by constant nagging, bribing and yelling, they don't know what to try next. Some parents worry that their children are unhappy. Struggling at school, not making friends or coping with bigger problems.

The good news is that getting your children to behave more co-operatively doesn't need to be difficult or mysterious. We all know that kids don't come with manuals, but there are skills every parent can learn to make parenting easier. In a few sessions with a Parenting Psychologist, you will receive step by step guidance in how to talk to your children in a way that will be much more effective getting them to behave in a respectful and co-operative way around the home and in public. You will learn how to help your child cope with problems they are going through. They can help you reconnect with your kids so you can enjoy being a parent again.

Nice to have
• Themes consistent with our website
and letterhead, business cards. I will attach these.
Should not have
• I don't want it to look too cluttered so if the text I have provided up above looks too crowded then I will edit it.

```html
<!DOCTYPE html>
<html lang="en">
<head>
<meta charset="utf-8">
<title>Parenting Psychologists – Wellmind Counselling Centre</title>
<link rel="stylesheet" href="https://fonts.googleapis.com/css2?family=Arimo:wght@400;700&family=Roboto+Condensed:wght@700&display=swap">
<style>
  :root {
    --band-1: #6a9c80;
    --band-2: #8fc6c8;
    --band-3: #6ea3a6;
    --band-4: #7c8a96;
    --band-5: #3f7f7c;
    --band-6: #8ccfd0;
    --band-7: #3e3e3e;
    --band-8: #9b9677;
    --paper-top: #f6f6f4;
    --paper-mid: #dfe0dd;
    --paper-low: #d2d3cf;
    --stripe: rgba(255,255,255,0.28);
    --ink: #2a2a2a;
    --headline: #333333;
    --footer-bg: #efefec;
    --footer-rule: #c9cac6;
  }
  * { margin: 0; padding: 0; box-sizing: border-box; }
  html, body { width: 1200px; height: 2439px; overflow: hidden; }
  body { background: var(--paper-mid); }

  .flyer {
    position: relative;
    width: 1200px;
    height: 2439px;
    overflow: hidden;
    background:
      linear-gradient(90deg, transparent 0 150px, var(--stripe) 150px 300px, transparent 300px 450px, var(--stripe) 450px 600px, transparent 600px 900px, var(--stripe) 900px 1050px, transparent 1050px),
      linear-gradient(180deg, var(--paper-top) 0%, var(--paper-top) 12%, var(--paper-mid) 55%, var(--paper-low) 88%);
  }

  .colour-bands { position: absolute; top: 0; left: 0; width: 1200px; height: 63px; display: flex; }
  .colour-bands span { flex: 1; }
  .colour-bands span:nth-child(1) { background: var(--band-1); }
  .colour-bands span:nth-child(2) { background: var(--band-2); }
  .colour-bands span:nth-child(3) { background: var(--band-3); }
  .colour-bands span:nth-child(4) { background: var(--band-4); }
  .colour-bands span:nth-child(5) { background: var(--band-5); }
  .colour-bands span:nth-child(6) { background: var(--band-6); }
  .colour-bands span:nth-child(7) { background: var(--band-7); }
  .colour-bands span:nth-child(8) { background: var(--band-8); }

  .headline {
    position: absolute; left: 163px; top: 286px; width: 960px;
    font-family: "Arimo", Arial, sans-serif; font-weight: 400;
    font-size: 64px; line-height: 76px; color: var(--headline);
    white-space: nowrap;
  }

  .copy {
    position: absolute; left: 163px; width: 960px;
    font-family: "Arimo", Arial, sans-serif; font-weight: 400;
    font-size: 36px; line-height: 53.6px; color: var(--ink);
    white-space: nowrap;
  }
  .copy strong { font-weight: 700; }
  .copy--problem { top: 697px; }
  .copy--solution { top: 1107px; }

  .copy--promise {
    position: absolute; left: 163px; top: 1773px;
    font-family: "Roboto Condensed", "Arial Narrow", sans-serif; font-weight: 700;
    font-size: 40px; line-height: 57.8px; color: var(--ink);
    white-space: nowrap;
  }

  .footer {
    position: absolute; left: 0; top: 2146px; width: 1200px; height: 293px;
    background: var(--footer-bg);
    border-top: 2px solid var(--footer-rule);
  }
  .contact {
    position: absolute; right: 627px; top: 44px; text-align: right;
    font-family: "Arimo", Arial, sans-serif; font-size: 27px; line-height: 41.5px;
    color: var(--ink); white-space: nowrap; font-style: normal;
  }
  .contact strong { font-weight: 700; }
  .brand-name {
    position: absolute; left: 640px; top: 78px;
    font-family: "Arimo", Arial, sans-serif; font-weight: 400;
    font-size: 38px; line-height: 50px;
    color: var(--ink);
  }
</style>
</head>
<body>
<main class="flyer">
  <div class="colour-bands" aria-hidden="true">
    <span></span><span></span><span></span><span></span><span></span><span></span><span></span><span></span>
  </div>

  <h1 class="headline">Parents want the best for<br>their kids. They want kids<br>that are happy, healthy and<br>well behaved.</h1>

  <p class="copy copy--problem"><strong>So why is it so hard?</strong> Parents of toddlers,<br>primary schoolers and teenagers alike say that<br>they are frustrated by constant nagging, bribing<br>and yelling, they don't know what to try next.<br>Some parents worry that their children are<br>unhappy. Struggling at school, not making<br>friends or coping with bigger problems.</p>

  <p class="copy copy--solution">The good news is that getting your children to<br>behave more co-operatively doesn't need to be<br>difficult or mysterious. We all know that kids<br>don't come with manuals, but there are skills<br>every parent can learn to make parenting easier.<br>In a few sessions with a Parenting Psychologist,<br>you will receive step by step guidance in how to<br>talk to your children in a way that will be much<br>more effective getting them to behave in a<br>respectful and co-operative way around the<br>home and in public.</p>

  <p class="copy--promise">You will learn how to help your child cope with<br>problems they are going through. They can help you<br>reconnect with your kids so you can enjoy being a<br>parent again.</p>

  <footer class="footer">
    <address class="contact">
      Suite 1, 2087 Tamworth Rd<br>
      Tamworth North 3118<br>
      <strong>Tel: 6352 1840 | Fax: 6352 1847</strong><br>
      <strong>www.wellmindcounsellingcentre.com.au</strong>
    </address>
    <div class="brand-name">Wellmind Counselling<br>Centre</div>
  </footer>
</main>
</body>
</html>
```